Redesign current business card for food company

i would like to redesign my business card. our company is food company, our product range from chips, juices, milk and etc (mostly dried food stuff).
I want o keep same logo but , the rest is open to new design.
you can check at our website about our company www.velqorafare.com

Target Market(s)

most of food company

Industry/Entity Type

Business

Contact Information for Business Card

I want to keep more to blue color...

Colors
3176b5
abd036

Requirements
Must have
• our old logo
Nice to have
• we do not mind to have nice material on bus card in order to accomplish nice design. for example: using spot uv, embossed and etc.

```html
<!DOCTYPE html>
<html lang="en">
<head>
<meta charset="utf-8">
<title>Velqora Business Card</title>
<link href="https://fonts.googleapis.com/css2?family=Roboto:wght@300;400;500&display=swap" rel="stylesheet">
<style>
  :root {
    --brand-blue: #3176b5;
    --brand-blue-light: #3f9bd0;
    --brand-green: #abd036;
    --ink-blue: #2a78bd;
    --paper: #ffffff;
    --paper-shade: #eef0f1;
    --backdrop: #e9e6e0;
  }
  * { margin: 0; padding: 0; box-sizing: border-box; }
  html, body { width: 1200px; height: 1023px; overflow: hidden; }
  body {
    background: var(--backdrop);
    font-family: "Roboto", sans-serif;
    position: relative;
  }
  .card {
    position: absolute;
    left: 240px;
    width: 720px;
    height: 411px;
    border-radius: 22px;
    overflow: hidden;
    box-shadow: 0 6px 18px rgba(0,0,0,0.18);
  }
  .card-front { top: 50px; background: linear-gradient(160deg, var(--paper) 40%, var(--paper-shade)); }
  .card-back { top: 520px; background: linear-gradient(135deg, var(--brand-blue) 10%, var(--brand-blue-light) 90%); }
  .card-bands { position: absolute; inset: 0; width: 100%; height: 100%; }

  .brand {
    position: absolute;
    display: flex;
    align-items: center;
    gap: 10px;
    font-weight: 500;
    color: var(--brand-blue);
  }
  .brand-dot { border-radius: 50%; background: var(--brand-green); flex: none; }
  .front-brand { left: 78px; top: 118px; font-size: 58px; letter-spacing: -1px; }
  .front-brand .brand-dot { width: 16px; height: 16px; }

  .divider {
    position: absolute;
    left: 82px; top: 206px;
    width: 290px; height: 1px;
    background: linear-gradient(90deg, var(--brand-blue), rgba(49,118,181,0));
  }
  .person { position: absolute; left: 84px; top: 218px; }
  .person-name { font-size: 26px; font-weight: 400; color: var(--ink-blue); }
  .person-title { font-size: 15px; color: var(--brand-green); margin-top: 2px; }

  .contact-list { position: absolute; list-style: none; }
  .contact-list li {
    display: flex; align-items: center; gap: 10px;
    font-size: 15px; font-weight: 300; color: var(--ink-blue);
    height: 28px;
    white-space: nowrap;
  }
  .contact-left { left: 86px; top: 294px; }
  .contact-right { left: 372px; top: 230px; }
  .icon {
    width: 22px; height: 22px; border-radius: 50%;
    border: 1.5px solid var(--brand-green);
    display: flex; align-items: center; justify-content: center;
    flex: none;
  }
  .icon svg { width: 12px; height: 12px; }

  .back-brand {
    left: 0; right: 0; top: 0; bottom: 0;
    justify-content: center;
    color: var(--paper);
    font-size: 120px;
    letter-spacing: -3px;
  }
  .back-brand .brand-dot { width: 30px; height: 30px; background: var(--paper); }
</style>
</head>
<body>

<section class="card card-front">
  <svg class="card-bands" viewBox="0 0 720 411" preserveAspectRatio="none">
    <path d="M0 0 H22 C40 140 40 280 70 411 H0 Z" fill="var(--brand-green)"/>
    <path d="M0 60 C18 180 22 300 44 411 H0 Z" fill="var(--brand-blue)"/>
    <path d="M720 0 V411 H700 C680 280 680 140 650 0 Z" fill="var(--brand-green)"/>
    <path d="M720 0 V350 C702 240 698 120 678 0 Z" fill="var(--brand-blue)"/>
  </svg>

  <div class="brand front-brand"><span class="brand-dot"></span>velqora</div>
  <div class="divider"></div>
  <div class="person">
    <p class="person-name">Darren Osterholt</p>
    <p class="person-title">President</p>
  </div>

  <ul class="contact-list contact-left">
    <li><span class="icon"><svg viewBox="0 0 12 12"><path d="M2 1 L4 1 L5 4 L3.6 5 C4.3 6.6 5.4 7.7 7 8.4 L8 7 L11 8 L11 10 C11 10.6 10.6 11 10 11 C5 11 1 7 1 2 C1 1.4 1.4 1 2 1Z" fill="var(--brand-green)"/></svg></span>555 014 2288</li>
    <li><span class="icon"><svg viewBox="0 0 12 12"><rect x="2" y="4" width="8" height="6" fill="var(--brand-green)"/><rect x="3.5" y="1" width="5" height="3" fill="none" stroke="var(--brand-green)"/></svg></span>555 014 2277</li>
    <li><span class="icon"><svg viewBox="0 0 12 12"><rect x="1" y="2.5" width="10" height="7" fill="none" stroke="var(--brand-green)"/><path d="M1 2.5 L6 7 L11 2.5" fill="none" stroke="var(--brand-green)"/></svg></span>darren@velqorafare.com</li>
  </ul>

  <ul class="contact-list contact-right">
    <li><span class="icon"><svg viewBox="0 0 12 12"><rect x="3" y="1" width="6" height="10" rx="1" fill="none" stroke="var(--brand-green)"/><circle cx="6" cy="9.3" r="0.7" fill="var(--brand-green)"/></svg></span>555 018 4567</li>
    <li><span class="icon"><svg viewBox="0 0 12 12"><circle cx="6" cy="6" r="5" fill="none" stroke="var(--brand-green)"/><ellipse cx="6" cy="6" rx="2" ry="5" fill="none" stroke="var(--brand-green)"/><path d="M1 6 H11" stroke="var(--brand-green)"/></svg></span>www.velqorafare.com</li>
    <li><span class="icon"><svg viewBox="0 0 12 12"><path d="M6 11 C3 7 2.5 5.5 2.5 4.5 A3.5 3.5 0 0 1 9.5 4.5 C9.5 5.5 9 7 6 11Z" fill="var(--brand-green)"/><circle cx="6" cy="4.5" r="1.3" fill="var(--paper)"/></svg></span>1847 Marren St. Ashfield CA 90001</li>
  </ul>
</section>

<section class="card card-back">
  <svg class="card-bands" viewBox="0 0 720 411" preserveAspectRatio="none">
    <path d="M0 0 H14 C26 140 28 280 48 411 H0 Z" fill="var(--brand-green)"/>
    <path d="M0 40 C12 170 16 300 30 411 H0 Z" fill="var(--brand-blue)"/>
  </svg>
  <div class="brand back-brand"><span class="brand-dot"></span>velqora</div>
</section>

</body>
</html>
```